Business cards and stationery for new company logo
TRV Enterprises
Business cards and stationery for new company logo - Construction
Creative Brief
Simple
Marcus Pellham
Owner
742 Wildrow Ave. Larkhaven, Nova Scotia K4T 2B5
marcus@trventerprises.ca
www.trventerprises.ca
Would like something sleek and corporate looking. Catchy. The logo that was designed has all those elements...I would like the bus cards and stationery to also have those.

```html
<!DOCTYPE html>
<html lang="en">
<head>
<meta charset="utf-8">
<title>TRV Enterprises – Business Card</title>
<link href="https://fonts.googleapis.com/css2?family=Open+Sans:wght@400;600;800&display=swap" rel="stylesheet">
<style>
  :root {
    --bg: #e4e6e8;
    --card-white: #f7f7f7;
    --card-black: #1c1c1c;
    --brand-red: #d4161c;
    --ink: #1c1c1c;
    --ink-soft: #555555;
    --on-dark: #e8e8e8;
  }
  * { margin: 0; padding: 0; box-sizing: border-box; }
  html, body { width: 1200px; height: 980px; overflow: hidden; }
  body {
    background: var(--bg);
    font-family: "Open Sans", Arial, sans-serif;
    position: relative;
  }
  .card {
    position: absolute;
    width: 700px;
    height: 400px;
    left: 250px;
    border-radius: 22px;
    overflow: hidden;
    box-shadow: 0 8px 24px rgba(0,0,0,0.18);
  }
  .card--front { top: 50px; background: var(--card-white); }
  .card--back  { top: 530px; background: var(--card-black); }

  .front-wave { position: absolute; inset: 0; width: 100%; height: 100%; }

  .wordmark {
    font-family: "Open Sans", Arial, sans-serif;
    font-weight: 800;
    text-transform: uppercase;
    letter-spacing: 1px;
    line-height: 1;
  }
  .card--front .wordmark {
    position: absolute; left: 52px; top: 52px;
    font-size: 44px; color: var(--ink);
  }
  .holder { position: absolute; left: 54px; top: 136px; }
  .holder__name {
    color: var(--brand-red); font-weight: 600; font-size: 20px; letter-spacing: 1px;
  }
  .holder__title {
    color: var(--ink-soft); font-size: 13px; letter-spacing: 2px; text-transform: uppercase; margin-top: 2px;
  }

  .contact {
    position: absolute; right: 40px; top: 190px;
    list-style: none; font-size: 13px; color: var(--ink); line-height: 1.55;
  }
  .contact li { display: flex; align-items: flex-start; gap: 8px; white-space: nowrap; }
  .contact svg { width: 12px; height: 12px; margin-top: 4px; flex: none; fill: var(--ink); }
  .contact .indent { padding-left: 20px; }

  .card--back .wordmark {
    position: absolute; left: 0; right: 0; top: 150px; text-align: center;
    font-size: 56px; color: var(--on-dark);
  }
  .back-web {
    position: absolute; left: 0; right: 0; top: 236px; text-align: center;
    color: var(--on-dark); font-size: 14px; letter-spacing: 5px; text-transform: uppercase;
  }
</style>
</head>
<body>

<section class="card card--front" aria-label="Business card front">
  <svg class="front-wave" viewBox="0 0 700 400" preserveAspectRatio="none" aria-hidden="true">
    <path d="M0 255 C 150 240, 260 300, 360 340 C 440 372, 560 390, 700 360 L700 400 L0 400 Z" fill="var(--card-black)"/>
    <path d="M0 232 C 160 215, 280 280, 380 322 C 470 358, 580 372, 700 340 L700 350 C 580 382, 470 372, 380 336 C 280 296, 160 236, 0 250 Z" fill="var(--brand-red)"/>
  </svg>

  <div class="wordmark">TRV Enterprises</div>

  <div class="holder">
    <div class="holder__name">Marcus Pellham</div>
    <div class="holder__title">Owner</div>
  </div>

  <ul class="contact">
    <li><svg viewBox="0 0 12 12"><path d="M6 0a4 4 0 0 0-4 4c0 3 4 8 4 8s4-5 4-8a4 4 0 0 0-4-4zm0 5.5A1.5 1.5 0 1 1 6 2.5a1.5 1.5 0 0 1 0 3z"/></svg>742 Wildrow Ave.</li>
    <li class="indent">Larkhaven, Nova Scotia K4T 2B5</li>
    <li><svg viewBox="0 0 12 12"><path d="M2.5 0.5l2 2-1 1.5c.8 1.6 2 2.8 3.5 3.5l1.5-1 2 2-1.5 2C5 10 1.5 6.5.5 2z"/></svg>902-555-0142</li>
    <li><svg viewBox="0 0 12 12"><path d="M0 2h12v8H0zm1 1v.3l5 3.2 5-3.2V3zm0 1.5V9h10V4.5L6 7.7z"/></svg>marcus@trventerprises.ca</li>
    <li><svg viewBox="0 0 12 12"><circle cx="6" cy="6" r="5.5"/></svg>www.trventerprises.ca</li>
  </ul>
</section>

<section class="card card--back" aria-label="Business card back">
  <div class="wordmark">TRV Enterprises</div>
  <div class="back-web">www.trventerprises.ca</div>
</section>

</body>
</html>
```